Window Company website re-design

We are creating a new website design for http://brindlepanes.com and we are going to be using wordpress for the site. The idea is to make it appeal to homeowners, more than half of the visitors will be female so the design must appeal to them with appropriate colors and shapes. Historically the website has been dark with a black background and the idea is to keep some of that but make it much brighter with textures and inviting colors.
Major competitors which we will mimic are the following in order of favorites:
http://www.harlowmeadow.com/ (this is something we really like because of the full width, call to action, easy to navigate, space for
http://www.quarrygateandyard.com/ (this is a nice wide design with a lot of great image space and call to actions)
http://www.refitbyoakridgeplu.com/ (the full width is nice here)
http://www.tidelinepanes.com/ (the slide over option showing the window is nice here.)
Others:
http://www.vorbek.com/
http://www.tosca.com/home/default.aspx
http://www.whitlockpanels.com/
https://www.glazeplanet.com/
http://www.dorset.com/

Brindle is the leader in the industry so they want a design that is going to portray that. The owners say that their competitors always copy what they do so this design must be cutting edge.

Important elements need to included:
1. Make the design convey very obviously they are a replacement window and door company.
2. Very clear “request a free estimate” call to action box on the homepage.
3. Area for the “Live Support” call to action
4. Navigation:

- Home
- Why Brindle
o Saves Dollars, Makes Sense
o We Have You Covered Start to Finish
o The Brindle Difference
o Pitfalls to Avoid
- Windows and Doors
o Windows
 Double Hung Windows
 Awning Windows
 Basement Hopper Windows
 Bow Windows
 Garden Windows
 Casement Windows
 Bay Windows
 Slider Windows
 Dead-Lite / Specialty / Transom
o Doors
 Storm Doors
 Brindle French Doors
 Patio Slider Doors
 Door Catalog
 Keypad Deadbolt
o Before and After
- About Us
o Testimonials
o Directions
o Warranty
o Employment
o Manufacturing process
o Home Shows
o Community Involvement
- Financing
- Commercial Division
- Careers
- Contact Us

Important elements for the Home Page:
1. Call to action – request a free quote
2. Awards
3. Live support
4. Guarantee
5. Featured testimonials
6. Press releases
7. Locations (Map?)

The attached photos can be used for the homepage images

Target Market(s)

The target market is middle income home owners who want good quality and great service.

Font styles to use
Sans Serif

Colors

Designer to choose colors to be used in the design.

Requirements
Must have
• We will need 2 designs, one for the homepage and the other for the inner pages.

2. Awards
3. Live support
4. Guarantee
5. Featured testimonials
6. Press releases
7. Locations (Map?)

```html
<!DOCTYPE html>
<html lang="en">
<head>
<meta charset="utf-8">
<title>Brindle Windows</title>
<link href="https://fonts.googleapis.com/css2?family=Ubuntu:wght@400;500;700&display=swap" rel="stylesheet">
<style>
:root{
  --black:#000;
  --ink:#222;
  --body:#555;
  --blue:#1b8be0;
  --tab:#dcdcdc;
  --panel:#f1f1f1;
  --line:#cfcfcf;
  --field:#ededed;
  --red:#8c1010;
  --orange:#f29a0e;
  --foot-text:#ddd;
}
*{box-sizing:border-box;margin:0;padding:0}
html,body{width:899px;height:1200px;overflow:hidden}
body{background:var(--black);font-family:"Ubuntu",sans-serif;color:var(--body);position:relative}
.abs{position:absolute}
h2,h3{font-weight:400}
.page-column{left:100px;top:0;width:699px;height:1050px;background:linear-gradient(#000 0,#000 80px,#3b3b3b 150px,#8a8a8a 300px,#e5e5e5 420px,#f6f6f6 520px,#f7f7f7 100%)}
.logo{display:flex;align-items:center;gap:8px;color:#fff;font-size:26px;font-weight:500;line-height:1}
.logo i{width:22px;height:22px;background:#fff;display:block}
.call{left:480px;top:44px;color:#fff;font-size:11px}
.call b{font-size:18px;font-weight:400;margin-left:3px}
.live{left:648px;top:18px;width:130px;height:50px;border-radius:6px;background:linear-gradient(#5a5a5a,#262626);border:1px solid #666}
.live-avatar{left:6px;top:5px;width:38px;height:40px;border-radius:50%;background:linear-gradient(#c9a57f,#8a6a4c)}
.live-title{left:48px;top:10px;color:#fff;font-size:10.5px;font-weight:700}
.live-status{left:54px;top:26px;width:64px;height:11px;border-radius:3px;background:var(--orange);color:#fff;font-size:8px;font-weight:700;text-align:center;line-height:11px}
.nav{left:116px;top:74px;width:666px;height:32px;background:linear-gradient(#333,#111);border:1px solid #444;display:flex;overflow:hidden}
.nav a{flex:1 1 auto;text-align:center;color:#eee;text-decoration:none;font-size:11px;line-height:30px;padding:0 6px;border-right:1px solid #444;white-space:nowrap}
.nav a.current{background:#4a4a4a}
.nav a.drop::after{content:"";display:inline-block;margin-left:4px;border:3px solid transparent;border-top:4px solid #eee;vertical-align:-1px}
.slider{left:116px;top:112px;width:666px;height:272px;border:3px solid #fff;background:linear-gradient(#9fb7cf 0,#b9c7d3 22%,#8a6a55 30%,#7a5a48 70%,#6f7d4a 90%,#585f3a 100%)}
.slider-caption{left:0;bottom:0;width:100%;height:32px;background:rgba(0,0,0,.7);color:#fff;font-size:17.5px;line-height:32px;padding-left:10px}
.dots{left:660px;top:372px;display:flex;gap:5px}
.dots span{width:19px;height:19px;border-radius:50%;background:#fff;border:2px solid #111;font-size:10px;font-weight:700;color:#111;text-align:center;line-height:15px}
.quote{left:122px;top:414px;width:654px;height:96px;background:linear-gradient(#fafafa,#dedede);border:2px solid #bdbdbd;border-radius:5px;box-shadow:0 4px 6px rgba(0,0,0,.2)}
.tab{background:var(--tab);color:var(--blue);text-align:center;border-radius:2px;box-shadow:0 1px 2px rgba(0,0,0,.2)}
.quote-title{left:350px;top:411px;width:198px;height:29px;font-size:17px;line-height:29px}
.field{background:var(--field);border:1px solid #d6d6d6;color:#666;font-size:9px;padding:3px 6px;height:19px}
.select::after{content:"";position:absolute;right:0;top:0;width:16px;height:17px;background:#ddd;border-left:1px solid #ccc}
.select::before{content:"";position:absolute;right:4px;top:7px;border:4px solid transparent;border-top:5px solid #333;z-index:1}
.submit{left:706px;top:474px;width:64px;height:23px;border-radius:3px;background:linear-gradient(#555,#111);border:1px solid #999;color:#fff;font-size:12px;text-align:center;line-height:21px;letter-spacing:.5px}
.card{top:532px;width:156px;height:112px;background:linear-gradient(#fdfdfd,#ececec);border:1px solid #d2d2d2;border-radius:4px}
.card-tab{top:529px;width:120px;height:22px;font-size:11px;line-height:22px}
.card-icon{top:558px;height:28px}
.card-text{top:590px;width:142px;font-size:8.3px;line-height:11px;color:#444}
.more{font-size:8.5px;color:#333;font-weight:500}
.more::after{content:"";display:inline-block;margin-left:3px;border:2.5px solid transparent;border-left:3px solid #333}
.rule{left:117px;width:665px;height:1px;background:var(--line)}
.h2{font-size:13.5px;color:var(--ink)}
.guarantee-img{left:117px;top:692px;width:100px;height:94px;border-radius:3px;border:1px solid #bbb;background:linear-gradient(#8ab0d6,#b5c8d8 35%,#8a3a2a 60%,#6b7a45)}
.welcome-text{left:230px;top:692px;width:376px;font-size:8.4px;line-height:11.7px;color:#777;text-align:justify}
.badge{border-radius:4px}
.lower{left:120px;top:816px;width:658px;height:214px;background:#fafafa;border:1px solid #dadada;border-radius:4px}
.lower-split{left:451px;top:830px;width:1px;height:190px;background:#ddd}
.lower-tab{top:814px;width:119px;height:22px;font-size:11px;line-height:22px}
.arrows{display:flex;gap:5px}
.arrows span{width:16px;height:16px;border-radius:50%;border:1px solid #bbb;background:#eee;position:relative}
.arrows span::after{content:"";position:absolute;top:4px;border:3px solid transparent}
.arrows .prev::after{left:3px;border-right:4px solid #333}
.arrows .next::after{left:6px;border-left:4px solid #333}
.release h3{font-size:11px;color:var(--ink);margin-bottom:4px}
.release p{font-size:8.4px;line-height:12px;color:#444;margin-bottom:4px}
.video{left:487px;top:846px;width:255px;height:156px;background:#111;padding:4px}
.video-frame{width:100%;height:100%;background:linear-gradient(90deg,#3a3a3a,#6b6258 50%,#c9c3b8)}
.video-bar{left:491px;top:980px;width:247px;height:18px;background:rgba(0,0,0,.75);color:#fff;font-size:8px;display:flex;align-items:center;gap:6px;padding:0 6px}
.video-bar .track{flex:1;height:4px;border-radius:2px;background:#444}
.video-base{left:464px;top:1002px;width:305px;height:10px;background:linear-gradient(#a01818,#5c0808);border-radius:0 0 3px 3px}
.footer{left:0;top:1050px;width:899px;height:122px;background:#000}
.foot-h{font-size:13.5px;color:#eee}
.links{font-size:8.5px;color:var(--foot-text);list-style:none;line-height:20.5px}
.links li::before{content:"";display:inline-block;width:2.5px;height:2.5px;background:#ddd;margin-right:6px;vertical-align:2px}
.map{left:342px;top:1086px;width:108px;height:78px;border:2px solid #fff;background:linear-gradient(135deg,#efe6c8,#f3eed8 50%,#cfe0f2 80%)}
.foot-field{background:#fff;color:#777;font-size:9px;padding:5px 6px;width:140px}
.foot-btn{left:485px;top:1148px;width:67px;height:18px;background:linear-gradient(#aaa,#777);border-radius:2px;color:#111;font-size:9px;text-align:center;line-height:18px}
.social{left:654px;top:1149px;display:flex;gap:14px}
.social span{width:16px;height:16px;border-radius:50%;background:#ccc}
.copyright{left:0;top:1172px;width:899px;height:28px;background:#3a3a3a;color:#ddd;font-size:9.5px;text-align:center;line-height:24px}
</style>
</head>
<body>
<div class="abs page-column"></div>

<header>
  <div class="abs logo" style="left:130px;top:22px"><i></i>Brindle</div>
  <div class="abs call">Call Us <b>800-555-0147</b></div>
  <div class="abs live">
    <div class="abs live-avatar" role="img" aria-label="Support agent portrait"></div>
    <div class="abs live-title">LIVE SUPPORT</div>
    <div class="abs live-status">ONLINE ▸</div>
  </div>
  <nav class="abs nav">
    <a class="current">Home</a>
    <a class="drop">Why Brindle</a>
    <a class="drop">Windows and Doors</a>
    <a class="drop">About Us</a>
    <a>Financing</a>
    <a>Commercial Division</a>
    <a>Careers</a>
    <a style="border-right:0">Contact Us</a>
  </nav>
</header>

<section class="abs slider" role="img" aria-label="Brick two-storey home with new replacement windows">
  <div class="abs slider-caption">Replacement Windows, Saves Energy And Increase Comfort</div>
</section>
<div class="abs dots"><span>1</span><span>2</span><span>3</span><span>4</span><span>5</span></div>

<section>
  <div class="abs quote"></div>
  <div class="abs tab quote-title">Request a free Quote</div>
  <div class="abs field" style="left:136px;top:455px;width:99px">Name</div>
  <div class="abs field" style="left:262px;top:455px;width:99px">Phone</div>
  <div class="abs field" style="left:136px;top:479px;width:99px">Email</div>
  <div class="abs field select" style="left:262px;top:479px;width:131px">Intrested Product</div>
  <div class="abs field" style="left:407px;top:455px;width:291px;height:43px">Message</div>
  <div class="abs submit">SUBMIT</div>
</section>

<section>
  <div class="abs card" style="left:117px"></div>
  <div class="abs card" style="left:286px"></div>
  <div class="abs card" style="left:457px"></div>
  <div class="abs card" style="left:626px"></div>
  <div class="abs tab card-tab" style="left:135px">WINDOWS</div>
  <div class="abs tab card-tab" style="left:304px">DOORS</div>
  <div class="abs tab card-tab" style="left:475px">BEFORE AND AFTER</div>
  <div class="abs tab card-tab" style="left:644px">MANUFACTURING</div>

  <svg class="abs card-icon" style="left:185px" width="20" height="28" viewBox="0 0 20 28" fill="none" stroke="#222" stroke-width="2"><path d="M2 4 L18 1 V27 L2 24 Z M10 3 V26 M2 14 H18"/></svg>
  <svg class="abs card-icon" style="left:350px" width="28" height="28" viewBox="0 0 28 28"><rect x="2" y="4" width="24" height="22" fill="#222"/><rect x="6" y="2" width="11" height="25" fill="#fff" stroke="#222" stroke-width="2"/><rect x="8" y="6" width="7" height="7" fill="#222"/></svg>
  <svg class="abs card-icon" style="left:508px" width="54" height="28" viewBox="0 0 54 28" fill="none" stroke="#222" stroke-width="2"><path d="M2 4 L16 1 V27 L2 24 Z M9 3 V25 M2 14 H16"/><path d="M26 8 H52 L48 22 H22 Z M32 8 L28 22 M39 8 L35 22 M45 8 L41 22 M24 15 H50"/></svg>
  <div class="abs card-icon" style="left:674px;width:60px;background:linear-gradient(#333,#111);border-radius:3px" role="img" aria-label="Workers assembling window frames"></div>

  <p class="abs card-text" style="left:125px">Lorem ipsum dolor sit amet, consec tetuer adipiscing elit, sed diam non ummy nibh euismod tincidunt ut.<br><span class="more">More</span></p>
  <p class="abs card-text" style="left:295px">Lorem ipsum dolor sit amet, consec tetuer adipiscing elit, sed diam non ummy nibh euismod tincidunt ut.<br><span class="more">More</span></p>
  <p class="abs card-text" style="left:465px">Lorem ipsum dolor sit amet, consec tetuer adipiscing elit, sed diam non ummy nibh euismod tincidunt ut.<br><span class="more">More</span></p>
  <p class="abs card-text" style="left:635px">Lorem ipsum dolor sit amet, consec tetuer adipiscing elit, sed diam non ummy nibh euismod tincidunt ut.<br><span class="more">More</span></p>
</section>

<div class="abs rule" style="top:662px"></div>

<section>
  <h2 class="abs h2" style="left:117px;top:670px">Welcome to Brindle Windows</h2>
  <div class="abs guarantee-img" role="img" aria-label="Home with a 100% guarantee seal"></div>
  <p class="abs welcome-text">Lorem ipsum dolor sit amet, consectetuer adipiscing elit, sed diam nonummy nibh euismod tincidunt ut laoreet dolore magna aliquam erat volutpat. Ut wisi enim ad minim veniam, quis nostrud exerci tation ullamcorper suscipit lobortis nisl ut aliquip ex ea commodo consequat. Duis autem vel eum iriure dolor in hendrerit in vulputate velit esse molestie consequat, vel illum dolore eu feugiat nulla facilisis at vero eros et accumsan et iusto odio dignissim.Ut wisi enim ad minim veniam, quis nostrud exerci tation ullamcorper suscipit lobortis nisl ut aliquip ex ea commodo consequat. Duis autem vel eum iriure dolor in hendrerit in vulputate velit esse.<br><span class="more" style="line-height:24px">More</span></p>
</section>

<aside>
  <h2 class="abs h2" style="left:624px;top:670px">Awards</h2>
  <div class="abs badge" style="left:625px;top:700px;width:72px;height:16px;background:#1f3f8a"></div>
  <div class="abs badge" style="left:706px;top:700px;width:64px;height:24px;background:#1a5a8a"></div>
  <div class="abs badge" style="left:625px;top:733px;width:40px;height:48px;background:#8ea33a;border-radius:4px 4px 20px 20px"></div>
  <div class="abs badge" style="left:711px;top:748px;width:53px;height:33px;background:#3f8a3a;border-radius:50%"></div>
</aside>

<div class="abs rule" style="top:802px"></div>

<section>
  <div class="abs lower"></div>
  <div class="abs lower-split"></div>
  <div class="abs tab lower-tab" style="left:231px">PRESS RELEASES</div>
  <div class="abs tab lower-tab" style="left:550px">TESTIMONIALS</div>
  <div class="abs arrows" style="left:397px;top:823px"><span class="prev"></span><span class="next"></span></div>
  <div class="abs arrows" style="left:735px;top:823px"><span class="prev"></span><span class="next"></span></div>

  <article class="abs release" style="left:134px;top:845px;width:260px">
    <h3>Lorem ipsum dolor sit am</h3>
    <p>Lorem ipsum dolor sit amet, consectetuer adipiscing Duis autem vel eum iriure dolor in hendrerit in vulputate velit esse molestie consequat, vel illumsed diam nonummy nibh euismod tincidunt ut laoreedolore magna</p>
    <span class="more">More</span>
  </article>
  <article class="abs release" style="left:134px;top:945px;width:260px">
    <h3>Lorem ipsum dolor sit am</h3>
    <p>Lorem ipsum dolor sit amet, consectetuer adipiscing Duis autem vel eum iriure dolor in hendrerit in vulputate velit esse molestie consequat, vel illumsed diam nonummy nibh euismod tincidunt ut laoreedolore magna</p>
    <span class="more">More</span>
  </article>

  <div class="abs video"><div class="video-frame" role="img" aria-label="Customer video testimonial"></div></div>
  <div class="abs video-bar">
    <svg width="8" height="9" viewBox="0 0 8 9"><path d="M0 0 L8 4.5 L0 9 Z" fill="#fff"/></svg>
    <span>04:59</span><span class="track"></span><span>10:35</span>
  </div>
  <div class="abs video-base"></div>
</section>

<footer>
  <div class="abs footer"></div>
  <h2 class="abs foot-h" style="left:130px;top:1057px">Quick Links</h2>
  <ul class="abs links" style="left:128px;top:1081px">
    <li>Home</li><li>Why Brindle</li><li>Window and Doors</li><li>About Us</li>
  </ul>
  <ul class="abs links" style="left:235px;top:1081px">
    <li>Financing</li><li>Commercial Division</li><li>Careers</li><li>Contact Us</li>
  </ul>
  <h2 class="abs foot-h" style="left:341px;top:1057px">View Location</h2>
  <div class="abs map" role="img" aria-label="Map showing the showroom location"></div>
  <h2 class="abs foot-h" style="left:484px;top:1057px">Subscribe Newsletter</h2>
  <div class="abs foot-field" style="left:485px;top:1086px">Name</div>
  <div class="abs foot-field" style="left:485px;top:1117px">Email</div>
  <div class="abs foot-btn">SUBSCRIBE</div>
  <div class="abs logo" style="left:654px;top:1098px"><i></i>Brindle</div>
  <div class="abs social"><span></span><span></span><span></span><span></span></div>
  <div class="abs copyright">© 2014 brindlepanes.com. &nbsp;|&nbsp; All Rights Reserved.</div>
</footer>
</body>
</html>
```